Do it yourself Karten und Hochzeitsdeko selbstgemacht
Zielgruppe
Wir sind ein Bastelgeschäft. Wir bieten Materialien zum selber machen von Karten, Tischkarten,Menükarten, Gästebüchern, Fotoalben an.
Alle Materialien zur Anlassgestaltung, auch Tischdeko und Kerzen.
Zielgruppe: Junge Leute auf einer Hochzeitsmesse
Aufgabenstellung
Ich benötige einen Flyer in A5 Format. Einige Fotoausschnitte und Text. Romantisch.
Fotos von angefertigten Karten und Deko sind vorhanden.
Logo vorhanden, soll mit rein und Öffnungszeiten mit Internet
Text: Do it Yourself Karten und Hochzeitsdeko selbst gemacht!
Zeiten etc. bitte www.falten-und-kleben.example

```html
<!DOCTYPE html>
<html lang="de">
<head>
<meta charset="utf-8">
<title>Faltwerk – Flyer</title>
<link href="https://fonts.googleapis.com/css2?family=Encode+Sans+Condensed:wght@300;400;700&display=swap" rel="stylesheet">
<style>
  :root {
    --teal: #5b959b;
    --teal-dark: #2f5b61;
    --ink: #3c4547;
    --paper: #ffffff;
    --page-bg: #ffffff;
    --photo-light: #e9eaf0;
    --photo-mid: #c9cbd3;
    --photo-green: #4f6b45;
  }
  * { box-sizing: border-box; margin: 0; padding: 0; }
  html, body { width: 1200px; height: 848px; overflow: hidden; background: var(--page-bg); }
  body { position: relative; font-family: "Encode Sans Condensed", "Arial Narrow", sans-serif; color: var(--ink); }

  .flyer {
    position: absolute; top: 118px; width: 423px; height: 600px;
    background: var(--paper);
    box-shadow: 0 1px 4px rgba(0,0,0,.25);
    overflow: hidden;
  }
  .flyer--front { left: 134px; }
  .flyer--back { left: 644px; }

  .flyer__band {
    position: absolute; left: 0; top: 200px; width: 100%; height: 400px;
    background: var(--teal);
  }

  .brand-name {
    position: absolute; left: 0; width: 100%; top: 130px; text-align: center;
    font-weight: 300; font-size: 58px; line-height: 1; color: var(--teal);
    top: 12px; letter-spacing: 1px;
  }
  .brand-tagline {
    position: absolute; left: 0; width: 100%; top: 100px; text-align: center;
    font-weight: 300; font-size: 21px; color: var(--ink);
  }
  .headline {
    position: absolute; left: 0; width: 100%; top: 139px; text-align: center;
    font-weight: 700; font-size: 18.5px; color: var(--teal-dark); letter-spacing: .1px;
  }
  .subline {
    position: absolute; left: 0; width: 100%; top: 162px; text-align: center;
    font-weight: 300; font-size: 18.5px; color: var(--ink);
  }

  .photo { position: absolute; border: 2px solid #fff; }
  .photo--hero {
    left: 39px; top: 216px; width: 345px; height: 368px;
    background: linear-gradient(150deg, #8a8c90 0%, var(--photo-mid) 25%, var(--photo-light) 55%, #dcdde4 100%);
  }
  .photo__url {
    position: absolute; left: 0; width: 100%; bottom: 8px; text-align: center;
    padding-right: 40px;
    font-weight: 700; font-size: 13px; color: #fff;
  }

  .grid { position: absolute; left: 39px; top: 216px; width: 345px; height: 368px; background: #fff; }
  .grid .cell { position: absolute; }
  .cell--a { left: 2px; top: 2px; width: 168px; height: 121px; background: linear-gradient(160deg, #d7d9e2, #f1f1f4); }
  .cell--b { left: 172px; top: 2px; width: 171px; height: 243px; background: linear-gradient(180deg, #f2f2f2 0%, #cfd3cf 40%, var(--photo-green) 62%, #e5e5e5 100%); }
  .cell--c { left: 2px; top: 125px; width: 168px; height: 241px; background: linear-gradient(180deg, #cfd0d6 0%, #ececee 35%, var(--photo-green) 70%, #e6e4df 100%); }
  .cell--d { left: 172px; top: 247px; width: 171px; height: 119px; background: linear-gradient(150deg, #cfcfd4, #f0f0f2); }

  .seal {
    position: absolute; width: 108px; height: 108px; border-radius: 50%;
    background: var(--teal); border: 3px solid #fff;
    display: flex; flex-direction: column; align-items: center; justify-content: center;
    color: #fff;
  }
  .seal__name { font-weight: 400; font-size: 22px; line-height: 1; }
  .seal__tag { font-weight: 400; font-size: 9px; margin-top: 4px; letter-spacing: .3px; }
  .flyer--front .seal { left: 303px; top: 481px; }
  .flyer--back .seal { left: 158px; top: 345px; }

  .hours {
    position: absolute; left: 0; width: 100%; top: 32px; text-align: center;
    font-weight: 300; font-size: 13.5px; line-height: 16px; color: var(--ink);
  }
  .hours__title { font-weight: 700; color: var(--teal-dark); margin-bottom: 3px; }
  .hours p { margin-bottom: 3px; }
  .hours .web { font-weight: 700; color: var(--teal-dark); }
</style>
</head>
<body>

  <section class="flyer flyer--front">
    <div class="brand-name">Faltwerk</div>
    <div class="brand-tagline">Basteln &amp; Dekorieren</div>
    <h1 class="headline">DO-IT-YOURSELF-KARTEN &amp; HOCHZEITSDEKO</h1>
    <div class="subline">selbst gemacht</div>

    <div class="flyer__band"></div>
    <div class="photo photo--hero" role="img" aria-label="Foto: selbst gestaltete weiße Hochzeitskarten mit Herzmotiven und Organzaschleifen">
      <div class="photo__url">www.falten-und-kleben.example</div>
    </div>
    <div class="seal">
      <span class="seal__name">Faltwerk</span>
      <span class="seal__tag">Basteln &amp; Dekorieren</span>
    </div>
  </section>

  <section class="flyer flyer--back">
    <div class="hours">
      <p class="hours__title">Öffnungszeiten:</p>
      <p>Montag, Dienstag, Donnerstag und Freitag:<br>9.30 Uhr – 13.00 Uhr und 14.30 Uhr – 18.00 Uhr</p>
      <p>Mittwoch und Samstag:<br>9.30Uhr – 13.00Uhr</p>
      <p>Telefon: 01234.567890</p>
      <p>info@falten-und-kleben.example</p>
      <p class="web">www.falten-und-kleben.example</p>
    </div>

    <div class="flyer__band"></div>
    <div class="grid">
      <div class="cell cell--a" role="img" aria-label="Foto: Herzkarte mit Serviette"></div>
      <div class="cell cell--b" role="img" aria-label="Foto: Glas mit grünem Buchsbaumherz und Schleife"></div>
      <div class="cell cell--c" role="img" aria-label="Foto: Karte mit grünem Herzkranz und Satinband"></div>
      <div class="cell cell--d" role="img" aria-label="Foto: Menükarte neben einem Weinglas"></div>
    </div>
    <div class="seal">
      <span class="seal__name">Faltwerk</span>
      <span class="seal__tag">Basteln &amp; Dekorieren</span>
    </div>
  </section>

</body>
</html>
```